Pebble brook candles

Product label on glass and packages : hand made candles :colours white, black,red and Amber some type of image of light or of nature butterfly , birds ...
Back ground of dots or shapes , label should be square 80mm to 90mm
Target Market(s)
25year olds and up male and female
Industry/Entity Type
Home And Garden
Requirements
Must have
- White,black,red and Amber must be modern eclectic style, could also use just the first letters of name, layering of colour .
Nice to have
- Light flickering , or picture of dawn setting , butterfly's , birds
- Hand poured
- Scented candles

```html
<!DOCTYPE html>
<html lang="en">
<head>
<meta charset="utf-8">
<title>Pebble Brook Candles – Label</title>
<link href="https://fonts.googleapis.com/css2?family=Dancing+Script:wght@700&display=swap" rel="stylesheet">
<style>
  :root {
    --stage-grey: #808080;
    --ink-black: #0a0604;
    --glow-white: #fffbe0;
    --glow-yellow: #ffd21a;
    --amber: #f39a0c;
    --ember-red: #b0340a;
    --char-brown: #2a0a02;
  }
  html, body {
    margin: 0;
    padding: 0;
    width: 1200px;
    height: 1000px;
    overflow: hidden;
    background: var(--stage-grey);
  }
  .stage {
    position: relative;
    width: 1200px;
    height: 1000px;
  }
  .label {
    position: absolute;
    left: 413px;
    top: 376px;
    width: 374px;
    height: 249px;
    overflow: hidden;
  }
  .label__glow {
    position: absolute;
    inset: 0;
    background:
      radial-gradient(ellipse 40% 18% at 52% 50%, var(--glow-white) 0%, rgba(255,240,150,0.85) 45%, rgba(255,210,26,0) 100%),
      radial-gradient(ellipse 62% 46% at 52% 50%, var(--glow-yellow) 0%, var(--amber) 45%, var(--ember-red) 75%, var(--char-brown) 100%);
  }
  .brand {
    position: absolute;
    left: 58px;
    top: 88px;
    margin: 0;
    font-family: "Dancing Script", cursive;
    font-weight: 700;
    color: var(--ink-black);
    line-height: 1;
  }
  .brand__name {
    display: block;
    font-size: 40px;
    white-space: nowrap;
  }
  .brand__product {
    display: block;
    font-size: 19px;
    text-align: right;
    margin-top: -4px;
    margin-right: -14px;
  }
</style>
</head>
<body>
  <main class="stage">
    <section class="label">
      <div class="label__glow" role="img" aria-label="Glowing amber and red bokeh light particles radiating from a bright golden centre"></div>
      <h1 class="brand">
        <span class="brand__name">Pebble Brook</span>
        <span class="brand__product">Candles</span>
      </h1>
    </section>
  </main>
</body>
</html>
```